BrambleWorks business card

Looking for business card design that supports our company/software values. We have 2 logo designs at the moment but open to change if you think you can enhance the brand. Check out website www.brambleworks.com.au.

Target Market(s)

Education

Contact Information for Business Card

Name, title, mobile, email and website

Font styles to use
Sans Serif

Colors

Designer to choose colors to be used in the design.

Requirements
Must have
• BrambleWorks logo with tree and tagline on rear side with dark grey background colour

```html
<!DOCTYPE html>
<html lang="en">
<head>
<meta charset="utf-8">
<title>BrambleWorks business card</title>
<link href="https://fonts.googleapis.com/css2?family=Open+Sans:wght@700&family=PT+Sans:wght@400;700&display=swap" rel="stylesheet">
<style>
  :root {
    --backdrop: #cfdacd;
    --charcoal: #4b4848;
    --paper: #fbfbfa;
    --leaf: #3f8a35;
    --leaf-dark: #2d6a2a;
    --sun: #f0b323;
    --ink: #4a4747;
    --white: #ffffff;
  }
  * { margin: 0; padding: 0; box-sizing: border-box; }
  html, body {
    width: 1200px; height: 1200px; overflow: hidden;
    background: var(--backdrop);
  }
  body { position: relative; font-family: "PT Sans", sans-serif; }

  .card {
    position: absolute; top: 287px;
    width: 356px; height: 621px;
    background: var(--paper); overflow: hidden;
  }
  .card--front { left: 170px; }
  .card--back { left: 677px; }

  /* Front */
  .front__panel {
    position: absolute; left: 0; top: 0; width: 100%; height: 497px;
    background: var(--charcoal);
  }
  .brand-lockup {
    position: absolute; left: 0; right: 0; top: 150px; text-align: center;
    color: var(--white);
  }
  .brand-lockup__name {
    font-family: "PT Sans", sans-serif; font-weight: 400;
    font-size: 33px; line-height: 1; letter-spacing: 0.3px;
  }
  .brand-lockup__rule {
    width: 170px; height: 1px; margin: 9px auto 5px;
    background: rgba(255,255,255,0.7);
  }
  .brand-lockup__tagline { font-size: 13.5px; letter-spacing: 0.2px; }

  .person { position: absolute; left: 29px; top: 414px; color: var(--white); }
  .person__name {
    font-family: "Open Sans", sans-serif; font-weight: 700;
    font-size: 27px; line-height: 1;
  }
  .person__title {
    margin-top: 10px; font-size: 15px; letter-spacing: 5.2px;
  }

  .contact { position: absolute; left: 26px; top: 545px; color: var(--ink); font-size: 16.5px; }
  .contact__row { display: flex; align-items: center; gap: 6px; height: 29px; letter-spacing: 0.6px; }
  .contact__row--phone { padding-left: 3px; letter-spacing: 1.6px; }
  .contact__icon { flex: none; }

  /* Back */
  .back-brand {
    position: absolute; left: 22px; top: 60px;
    display: flex; align-items: center; gap: 10px;
  }
  .back-brand__dot { width: 22px; height: 22px; border-radius: 50%; background: var(--sun); }
  .back-brand__name { font-size: 31px; color: var(--ink); line-height: 1; letter-spacing: 0.5px; }

  .website {
    position: absolute; left: 55px; top: 206px;
    display: flex; align-items: center; gap: 8px;
    font-size: 17px; color: var(--ink); letter-spacing: 0.8px;
  }

  .branch-art {
    position: absolute; left: 39px; top: 265px; width: 317px; height: 356px;
    background: radial-gradient(ellipse at 85% 35%, #5b5857 0%, #7a8a6f 35%, rgba(63,138,53,0.35) 65%, rgba(251,251,250,0) 85%);
  }
</style>
</head>
<body>

<section class="card card--front" aria-label="Card front">
  <div class="front__panel">
    <div class="brand-lockup">
      <div class="brand-lockup__name">BrambleWorks</div>
      <div class="brand-lockup__rule"></div>
      <div class="brand-lockup__tagline">Student Success Platform</div>
    </div>
    <div class="person">
      <div class="person__name">Clara Hughes</div>
      <div class="person__title">HR MANAGER</div>
    </div>
  </div>

  <div class="contact">
    <div class="contact__row contact__row--phone">
      <svg class="contact__icon" width="14" height="22" viewBox="0 0 14 22" aria-hidden="true">
        <rect x="1" y="1" width="12" height="20" rx="2" fill="none" stroke="var(--leaf)" stroke-width="2"/>
        <circle cx="7" cy="17.5" r="1.2" fill="var(--leaf)"/>
      </svg>
      <span>555.014.2290</span>
    </div>
    <div class="contact__row">
      <svg class="contact__icon" width="22" height="16" viewBox="0 0 22 16" aria-hidden="true">
        <rect x="0" y="0" width="22" height="16" fill="var(--leaf)"/>
        <path d="M0 0 L11 9 L22 0" fill="none" stroke="var(--paper)" stroke-width="1.6"/>
        <path d="M0 16 L8 7 M22 16 L14 7" stroke="var(--paper)" stroke-width="1.2"/>
      </svg>
      <span>hr.clara@brambleworks.com.au</span>
    </div>
  </div>
</section>

<section class="card card--back" aria-label="Card back">
  <div class="back-brand">
    <span class="back-brand__dot"></span>
    <span class="back-brand__name">BrambleWorks</span>
  </div>

  <div class="website">
    <svg width="22" height="22" viewBox="0 0 22 22" aria-hidden="true">
      <circle cx="11" cy="11" r="10" fill="var(--leaf-dark)"/>
      <ellipse cx="11" cy="11" rx="4.5" ry="10" fill="none" stroke="var(--paper)" stroke-width="1.3"/>
      <path d="M1 11 H21 M3 6 H19 M3 16 H19" stroke="var(--paper)" stroke-width="1.3"/>
    </svg>
    <span>brambleworks.com.au</span>
  </div>

  <div class="branch-art" role="img" aria-label="Illustration of a grey willow branch with green leaves reaching in from the right edge"></div>
</section>

</body>
</html>
```